Make a website for Velmora, a Luxury and Modern Concierge Platform based in the UAE

Concierge Platform that has various luxury and exotic actives available to clients, itinerary planning for a dubai / uae based holiday.
Want the website to appear luxury, modern and easy to understand, with a landing page that can captivate customers, majority will use Mobile but Desktop should look good too. Whatsapp Contact pop-out, and email sign up list. Social Link (Facebook, Instagram, Whatsapp, Whatsapp Broadcast, Twitter/X, etc).
Ability to make it Dark and Light themed.
Second page Page that has a list of activities on a drop down/ list, as follows:
Flights
Car Rental
Luxury Car Rental
Chauffer
Yachts/ Boats
Jet Ski / Watersports
Buggies/ ATV
Dining
Tickets/Events
Apartments/ Hotels
Personal Shopping.
Link to competitors, who's websites appear basic and could be 100% improved, for examples:
- https://www.quietharbourstays.example/
- https://www.tivra.example/
- https://www.gulf-latch.example/
- https://thelomarenhouse.example/dubai.html
- https://www.theplatinumhostdesk.example/concierge-service-dubai/
Open to logo designs, we own Velmora.com.
Colours:
Luxury Style, Black and Gold is often used, but maybe over-used?
A modern colour palette White, Light Blue, Light Grey, but we aren't experts at this, so this isn't by any means strict criteria, let the creative mind run free.
Thank you

```html
<!DOCTYPE html>
<html lang="en">
<head>
<meta charset="utf-8">
<title>Velmora — Luxury and Modern Concierge</title>
<link rel="stylesheet" href="https://fonts.googleapis.com/css2?family=Montserrat:wght@400;500;600;700&family=Questrial&display=swap">
<style>
:root{
  --blue:#7cc8e6;
  --blue-deep:#4aa6d6;
  --blue-line:#5ab8de;
  --ink:#111;
  --text:#333;
  --muted:#555;
  --grey-bg:#ececec;
  --white:#fff;
  --field-line:#d6d6d6;
}
*{margin:0;padding:0;box-sizing:border-box}
html,body{width:1200px;height:4129px;overflow:hidden}
body{position:relative;background:var(--white);font-family:'Questrial',sans-serif;color:var(--text)}
.abs{position:absolute}
.heading{font-family:'Montserrat',sans-serif;font-weight:500;color:var(--ink);letter-spacing:0.5px}
.underline{position:absolute;height:3px;width:64px;background:var(--blue-line);border-radius:2px}
.btn{position:absolute;display:flex;align-items:center;justify-content:center;border-radius:26px;font-family:'Montserrat',sans-serif;font-weight:700;font-size:14px;letter-spacing:2.2px;text-transform:uppercase}
.btn-blue{background:var(--blue);color:var(--white)}
.btn-white{background:var(--white);color:var(--blue)}

/* header */
.site-header{position:absolute;left:0;top:0;width:1200px;height:80px;background:#f7f7f7;border-bottom:1px solid #e2e2e2}
.logo{position:absolute;font-family:'Montserrat',sans-serif;font-weight:500;color:var(--ink);letter-spacing:4px}
.site-header .logo{left:77px;top:22px;font-size:28px}
.nav a{position:absolute;top:34px;font-family:'Montserrat',sans-serif;font-size:13px;letter-spacing:1.6px;color:#333;text-decoration:none}
.nav .active::after{content:"";position:absolute;left:0;right:0;bottom:-10px;height:2px;background:var(--blue-line)}

/* hero */
.hero-photo{position:absolute;left:0;top:80px;width:1200px;height:612px;background:linear-gradient(180deg,#dfe9f0 0%,#b9d2e0 22%,#4b86a6 40%,#2f6d90 62%,#3d7ea0 80%,#8ea9bb 100%)}
.hero-title{position:absolute;left:0;width:1200px;top:182px;text-align:center;font-size:42px}
.hero-sub{position:absolute;left:0;width:1200px;top:247px;text-align:center;font-size:27px}
.hero-dots span{position:absolute;left:20px;width:12px;height:12px;border-radius:50%;background:#fff}
.hero-dots span.current{background:transparent;border:2px solid #fff}

/* about */
.about-ring{position:absolute;left:-4px;top:755px;width:557px;height:517px;border:2px solid var(--blue);border-left:none;border-radius:0 260px 260px 0}
.about-photo{position:absolute;left:0;top:761px;width:545px;height:505px;border-radius:0 252px 252px 0;background:linear-gradient(180deg,#5b8fbf 0%,#a9bfd6 35%,#f0c9a0 55%,#c98f7a 65%,#6e89a6 85%,#4a6382 100%)}
.about-dot{position:absolute;left:422px;top:783px;width:54px;height:54px;border-radius:50%;background:var(--blue)}
.body-copy{font-size:16.5px;line-height:27px;color:var(--text)}

/* services */
.services{position:absolute;left:0;top:1349px;width:1200px;height:642px;background:linear-gradient(90deg,#f4f4f4 0%,#e4e4e4 60%,#dadada 100%)}
.service-card{position:absolute;width:311px;height:362px;border-radius:64px 0 64px 0;overflow:hidden}
.service-card .label{position:absolute;left:38px;bottom:26px;font-family:'Montserrat',sans-serif;font-size:21px;color:#fff;letter-spacing:0.3px;white-space:nowrap}
.pager span{position:absolute;top:1926px;width:48px;height:3px;border-radius:2px;background:#a8a8a8}
.pager span.current{background:var(--blue-line)}

/* why */
.why{position:absolute;left:0;top:1991px;width:1200px;height:601px;background:linear-gradient(90deg,#5fb4df 0%,#86cbea 55%,#a3d9ef 100%)}
.why .heading{color:#fff}
.why-photo{position:absolute}

/* testimonials */
.quote-card{position:absolute;left:288px;top:2754px;width:611px;height:272px;background:#fff;box-shadow:0 2px 10px rgba(0,0,0,0.18)}
.arrow{position:absolute}

/* contact */
.contact-bg{position:absolute;left:0;top:3124px;width:1200px;height:649px;background:linear-gradient(170deg,#cfe8f2 0%,#9fd2e3 30%,#7fc3d6 55%,#b8dde8 75%,#e9f3f6 100%)}
.field{position:absolute;background:#fff;border:1px solid var(--field-line);font-family:'Montserrat',sans-serif;font-size:16px;color:#333;padding:18px 26px}

/* footer */
.foot-head{position:absolute;font-family:'Montserrat',sans-serif;font-weight:700;font-size:15px;letter-spacing:2.5px;color:#222}
.foot-links a{position:absolute;left:359px;font-family:'Montserrat',sans-serif;font-size:14px;color:#333;text-decoration:none}
.social span{position:absolute;top:3835px;width:28px;height:28px;border-radius:50%;border:3px solid var(--blue-deep)}
.legal{position:absolute;top:4081px;font-family:'Montserrat',sans-serif;font-size:12px;color:#333}
</style>
</head>
<body>

<header class="site-header">
  <div class="logo">Velmora</div>
  <nav class="nav">
    <a class="active" style="left:301px">YACHTS</a>
    <a style="left:402px">EXPERIENCES</a>
    <a style="left:541px">RESERVATIONS</a>
    <a style="left:695px">LUXURY STAY</a>
    <a style="left:836px">CORPORATE</a>
    <a style="left:969px">CONCIERGE</a>
  </nav>
  <svg class="abs" style="left:1100px;top:33px" width="16" height="16" viewBox="0 0 16 16" aria-label="Search"><circle cx="6.5" cy="6.5" r="5" fill="none" stroke="#222" stroke-width="2"/><line x1="10.2" y1="10.2" x2="14.5" y2="14.5" stroke="#222" stroke-width="2.2" stroke-linecap="round"/></svg>
</header>

<section>
  <div class="hero-photo" role="img" aria-label="Woman relaxing on the deck of a white yacht on open blue sea with small islands on the horizon"></div>
  <h1 class="heading hero-title">Luxury and Modern Concierge</h1>
  <p class="heading hero-sub">Enjoy luxury and exotic activities</p>
  <a class="btn btn-blue" style="left:509px;top:301px;width:180px;height:50px">Learn more</a>
  <div class="hero-dots">
    <span class="current" style="top:326px"></span>
    <span style="top:343px"></span>
    <span style="top:361px"></span>
    <span style="top:379px"></span>
  </div>
</section>

<section>
  <div class="about-ring"></div>
  <div class="about-photo" role="img" aria-label="Passenger jet flying above clouds at sunset"></div>
  <div class="about-dot"></div>
  <h2 class="heading abs" style="left:605px;top:842px;font-size:42px">About Concierge</h2>
  <div class="underline" style="left:605px;top:901px"></div>
  <p class="body-copy abs" style="left:605px;top:924px;width:540px">Lorem ipsum dolor sit amet, consectetur adipiscing elit, sed do eiusmod tempor incididunt ut labore et dolore magna aliqua. Quis ipsum suspendisse ultrices gravida. Risus commodo viverra maecenas accumsan lacus vel facilisis.<br>Lorem ipsum dolor sit amet, consectetur adipiscing elit, sed do eiusmod tempor incididunt ut labore et dolore</p>
  <a class="btn btn-blue" style="left:599px;top:1113px;width:181px;height:52px">Learn more</a>
</section>

<section class="services"></section>
<h2 class="heading abs" style="left:0;width:1170px;text-align:center;top:1399px;font-size:42px">Our Services</h2>
<div class="underline" style="left:553px;top:1461px"></div>
<div class="service-card" style="left:77px;top:1506px;background:linear-gradient(160deg,#9cc4dc,#c9a98d 55%,#6b5a4a)" role="img" aria-label="Friends celebrating with champagne on a sailing yacht"><span class="label">YACHT PARTIES</span></div>
<div class="service-card" style="left:405px;top:1501px;background:linear-gradient(180deg,#6e94b3 0%,#c9d6de 45%,#5d6670 75%,#3f444a 100%)" role="img" aria-label="Private jet parked on a runway"><span class="label">PRIVATE JET</span></div>
<div class="service-card" style="left:731px;top:1497px;background:linear-gradient(180deg,#eef0f2 0%,#c9ccd0 50%,#2b2d31 80%,#5a5d62 100%)" role="img" aria-label="Couple stepping out of a black luxury car"><span class="label">LUXURY CAR RENTAL</span></div>
<div class="service-card" style="left:1058px;top:1493px;background:linear-gradient(160deg,#2b2a28,#8c7a62 50%,#3a3632)" role="img" aria-label="Leather interior of a chauffeured car"><span class="label" style="left:33px">CHAUFFEUR</span></div>
<div class="pager">
  <span class="current" style="left:518px"></span>
  <span style="left:579px"></span>
  <span style="left:638px"></span>
</div>

<section class="why"></section>
<h2 class="heading abs" style="left:120px;top:2080px;font-size:42px;line-height:44px;color:#fff">Why Choose<br>Concierge</h2>
<div class="underline" style="left:120px;top:2172px;background:#fff"></div>
<p class="body-copy abs" style="left:120px;top:2203px;width:520px;color:#fff">Lorem ipsum dolor sit amet, consectetur adipiscing elit, sed do eiusmod tempor incididunt ut labore et dolore magna aliqua. Quis ipsum suspendisse</p>
<p class="body-copy abs" style="left:120px;top:2317px;width:520px;color:#fff">Atrices gravida. Risus commodo viverra maecenas accumsan lacus vel facilisis. Lorem ipsum dolor sit amet, consectetur adipiscing elit, sed do eiusmo</p>
<a class="btn btn-white" style="left:111px;top:2427px;width:181px;height:50px">Learn more</a>
<div class="why-photo" style="left:665px;top:2103px;width:291px;height:422px;background:linear-gradient(160deg,#5a4634,#2c2a2c 50%,#4a4c52)" role="img" aria-label="Businessman on the phone in a private jet cabin"></div>
<div class="why-photo" style="left:968px;top:2041px;width:232px;height:420px;background:linear-gradient(170deg,#e9dcc6,#c7b59a 40%,#8c8478 70%,#3e3b38)" role="img" aria-label="Couple sitting on the bow of a sailing yacht"></div>

<section>
  <h2 class="heading abs" style="left:0;width:1200px;text-align:center;top:2652px;font-size:42px">What People Says</h2>
  <svg class="arrow" style="left:200px;top:2856px" width="24" height="46" viewBox="0 0 24 46" aria-label="Previous"><polyline points="22,2 2,23 22,44" fill="none" stroke="#333" stroke-width="2"/></svg>
  <svg class="arrow" style="left:956px;top:2856px" width="24" height="46" viewBox="0 0 24 46" aria-label="Next"><polyline points="2,2 22,23 2,44" fill="none" stroke="#333" stroke-width="2"/></svg>
  <div class="quote-card"></div>
  <svg class="abs" style="left:571px;top:2779px" width="46" height="36" viewBox="0 0 46 36" aria-hidden="true"><path d="M18 2C8 6 2 13 2 22a7 7 0 1 0 8-7c1-4 4-7 9-9z M42 2C32 6 26 13 26 22a7 7 0 1 0 8-7c1-4 4-7 9-9z" fill="var(--blue)"/></svg>
  <p class="body-copy abs" style="left:330px;top:2832px;width:527px;text-align:center">"Lorem ipsum dolor sit amet, consectetur adipiscing elit, sed do eiusmod tempor incididunt ut labore et dolore magna aliqua. Quis ipsum suspendisse ultrices gravida. Risus commodo viverra maecenas accumsan lacus vel facilisis"</p>
  <p class="abs" style="left:288px;width:611px;top:2962px;text-align:center;font-family:'Montserrat',sans-serif;font-weight:600;font-size:15px;color:#222">By Author Name</p>
  <div class="abs" style="left:399px;top:3023px;width:418px;height:4px;background:var(--blue-line)"></div>
</section>

<section>
  <div class="contact-bg" role="img" aria-label="Turquoise ocean wave breaking under bright sun"></div>
  <svg class="abs" style="left:0;top:3680px" width="1200" height="95" viewBox="0 0 1200 95" aria-hidden="true">
    <polygon points="0,95 0,68 665,20 1200,95" fill="#fff"/>
    <polygon points="665,20 1200,0 1200,92" fill="#8fd0ea"/>
  </svg>
  <h2 class="heading abs" style="left:0;width:1180px;text-align:center;top:3181px;font-size:42px">Contact Us</h2>
  <div class="underline" style="left:556px;top:3242px"></div>
  <div class="field" style="left:184px;top:3278px;width:404px;height:59px">First Name</div>
  <div class="field" style="left:602px;top:3278px;width:402px;height:59px">Last Name</div>
  <div class="field" style="left:184px;top:3353px;width:404px;height:61px">Email address</div>
  <div class="field" style="left:602px;top:3353px;width:402px;height:61px">Phone</div>
  <div class="field" style="left:184px;top:3428px;width:820px;height:101px">Message</div>
  <a class="btn" style="left:506px;top:3555px;width:192px;height:51px;background:var(--blue-deep);color:#fff">Submit now</a>
</section>

<footer>
  <div class="logo" style="left:114px;top:3791px;font-size:30px;font-weight:600">Velmora</div>
  <div class="foot-head" style="left:359px;top:3800px">QUICK LINKS</div>
  <nav class="foot-links">
    <a style="top:3837px">Yachts</a>
    <a style="top:3862px">Experiences</a>
    <a style="top:3887px">Reservations</a>
    <a style="top:3912px">Luxury stay</a>
    <a style="top:3937px">Corporate</a>
    <a style="top:3962px">Concierge</a>
  </nav>
  <div class="foot-head" style="left:559px;top:3797px">SIGN UP OUR EMAIL</div>
  <p class="abs" style="left:560px;top:3834px;font-family:'Montserrat',sans-serif;font-size:13px;color:#333">Please sign up here for latest updates.</p>
  <div class="abs" style="left:559px;top:3869px;width:276px;height:38px;border-radius:19px;background:#ececec;font-family:'Montserrat',sans-serif;font-size:12px;color:#333;padding:11px 20px">Email address</div>
  <a class="btn" style="left:564px;top:3922px;width:136px;height:37px;background:var(--blue-deep);color:#fff;font-size:11px">Subscribe</a>
  <div class="foot-head" style="left:892px;top:3797px">FOLLOW US</div>
  <div class="social">
    <span style="left:894px" role="img" aria-label="Social profile link"></span>
    <span style="left:941px" role="img" aria-label="Social profile link"></span>
    <span style="left:987px" role="img" aria-label="Social profile link"></span>
    <span style="left:1032px" role="img" aria-label="Social profile link"></span>
  </div>
  <div class="abs" style="left:0;top:4061px;width:1200px;height:1px;background:#e0e0e0"></div>
  <p class="legal" style="left:112px">© 2025 Company Name | All Rights Reserved</p>
  <p class="legal" style="left:860px">Privacy Policy</p>
  <p class="legal" style="left:972px">Terms of use</p>
</footer>

</body>
</html>
```